Digital Album Cover - Piano music for wedding ceremonies and receptions

I need cover art for a piano album project that will be distributed to TuneVault, Wavelane etc. Covert art required for front of album. At this stage physical CDs will not be printed nor required it is just a digital release.
Artist name: Toby Hargrove
Album Title: Gentle Keys Melodies Wedding Ceremonies and Receptions
Volume 3
Sample piano songs are on my tunecast page
https://tunecast.example/tobyhargrovekeys/sets/gentle-keys-melodies-vol-3
Previous album artwork used from sketch hive competitions winners
https://musicvault.example/au/artist/toby-hargrove/4830917265
Target Market(s)
brides to be
grooms to be
people interested in weddings
people enjoy love songs or easy listening music
Industry/Entity Type
Wedding
Look and feel
Each slider illustrates characteristics of the customer's brand and the style your logo design should communicate.

```html
<!DOCTYPE html>
<html lang="en">
<head>
<meta charset="utf-8">
<title>Gentle Keys Melodies – Toby Hargrove – Vol. 3</title>
<link rel="stylesheet" href="https://fonts.googleapis.com/css2?family=Antonio:wght@400;600;700&family=Saira+Extra+Condensed:wght@500&display=swap">
<style>
  :root {
    --stage: #151413;
    --cover-dark: #1c1d1c;
    --cover-mid: #3a3632;
    --cover-warm: #c9a58a;
    --cover-glow: #f3e3d2;
    --petal: #e8c3ad;
    --dress: #d9d3cc;
    --title: #f7f1ea;
    --title-warm: #f1dccb;
    --sub: #d8d2cb;
    --artist: #aaa8a1;
  }
  * { margin: 0; padding: 0; box-sizing: border-box; }
  html, body {
    width: 1200px; height: 960px; overflow: hidden;
    background: var(--stage);
  }
  .canvas {
    position: relative; width: 1200px; height: 960px;
  }
  .album-cover {
    position: absolute; left: 170px; top: 50px;
    width: 860px; height: 860px; overflow: hidden;
  }
  .cover-photo {
    position: absolute; inset: 0;
    background:
      radial-gradient(circle at 78% 8%, var(--cover-glow) 0%, rgba(243,227,210,0.55) 18%, rgba(201,165,138,0) 45%),
      radial-gradient(ellipse at 72% 62%, rgba(232,195,173,0.55) 0%, rgba(232,195,173,0) 30%),
      radial-gradient(ellipse at 80% 95%, rgba(217,211,204,0.6) 0%, rgba(217,211,204,0) 35%),
      linear-gradient(100deg, var(--cover-dark) 0%, var(--cover-dark) 28%, var(--cover-mid) 55%, var(--cover-warm) 100%);
  }
  .cover-type {
    position: absolute; left: 232px; top: 118px;
    width: 420px;
    color: var(--title);
  }
  .kicker {
    font-family: "Antonio", sans-serif; font-weight: 600;
    font-size: 22px; letter-spacing: 25px;
    text-transform: uppercase; margin-bottom: 10px;
  }
  .title-main, .title-second {
    font-family: "Antonio", sans-serif; font-weight: 700;
    text-transform: uppercase; line-height: 0.86;
    letter-spacing: -2px;
  }
  .title-main { font-size: 262px; color: var(--title); }
  .title-second { font-size: 138px; color: var(--title-warm); margin-top: 8px; }
  .occasion {
    font-family: "Saira Extra Condensed", sans-serif; font-weight: 500;
    font-size: 29px; letter-spacing: 1.5px; text-transform: uppercase;
    color: var(--sub); margin-top: 26px; white-space: nowrap;
  }
  .credit {
    display: flex; align-items: flex-end; gap: 16px;
    margin-top: 4px; white-space: nowrap;
  }
  .artist {
    font-family: "Antonio", sans-serif; font-weight: 400;
    font-size: 70px; line-height: 1; text-transform: uppercase;
    color: var(--artist); letter-spacing: -1px;
  }
  .volume {
    font-family: "Antonio", sans-serif; font-weight: 400;
    font-size: 40px; line-height: 1; text-transform: uppercase;
    color: var(--sub);
    border-left: 3px solid var(--sub); padding-left: 10px;
    margin-bottom: 4px;
  }
</style>
</head>
<body>
  <main class="canvas">
    <section class="album-cover">
      <div class="cover-photo" role="img" aria-label="Warm sunlit wedding photo of a couple, the bride holding a bouquet of cream tulips, peach roses and dark greenery"></div>
      <div class="cover-type">
        <p class="kicker">Gentle</p>
        <h1>
          <span class="title-main" style="display:block">Keys</span>
          <span class="title-second" style="display:block">Melodies</span>
        </h1>
        <p class="occasion">Wedding Ceremonies &amp; Receptions</p>
        <p class="credit">
          <span class="artist">Toby Hargrove</span>
          <span class="volume">Vol. 3</span>
        </p>
      </div>
    </section>
  </main>
</body>
</html>
```